Postcard Design

We need a postcard design for a private lender in the Denver area. We are offering hard money loans and loans for those doing fix-and-flips. We definitely want something that is Colorado-specific, maybe a view of downtown Denver? We are not offering small personal loans, but we are also not lending over 800k. Our audience is not major corporations. all the info in the old postcard is correct EXCEPT:

the new email should be thimble417@postvane.net

We would like to omit all use of exclamation points.

```html
<!DOCTYPE html>
<html lang="en">
<head>
<meta charset="utf-8">
<title>Harlow Peak Lending – Hard Money Loans Postcard</title>
<link href="https://fonts.googleapis.com/css2?family=Barlow+Condensed:wght@400;500;600&family=Roboto+Condensed:wght@400;700&family=Open+Sans:wght@400;600&family=Arimo:wght@400;700&display=swap" rel="stylesheet">
<style>
  :root {
    --backdrop: #2b3039;
    --blue-deep: #123f96;
    --blue-mid: #0a6ab8;
    --cyan: #0aa6e8;
    --cyan-light: #6ccaf2;
    --panel-grey: #e3e5e8;
    --purple: #6a2c91;
    --red: #ee1c25;
    --teal: #2196b6;
    --green: #76bd43;
    --stripe-blue: #00adee;
    --orange: #fbac1f;
    --ink: #111111;
    --white: #ffffff;
  }
  * { margin: 0; padding: 0; box-sizing: border-box; }
  html, body { width: 1200px; height: 1200px; overflow: hidden; background: var(--backdrop); }
  .stage { position: relative; width: 1200px; height: 1200px; }

  .card { position: absolute; left: 282px; width: 636px; height: 494px; overflow: hidden; }
  .card--front { top: 94px; background: var(--panel-grey); }
  .card--back { top: 611px; background: var(--white); }

  .front-art { position: absolute; inset: 0; }
  .brand-name {
    position: absolute; left: 64px; top: 24px;
    font-family: "Barlow Condensed", sans-serif; font-weight: 600;
    font-size: 40px; color: var(--white); letter-spacing: 0.2px;
  }
  .rate-badge {
    position: absolute; left: 504px; top: 60px; width: 106px; height: 106px;
    border-radius: 50%; background: var(--red); color: var(--white);
    text-align: center; font-family: "Roboto Condensed", sans-serif;
  }
  .rate-badge__label { display: block; font-size: 14px; line-height: 17px; margin-top: 14px; }
  .rate-badge__value { display: block; font-family: "Arimo", sans-serif; font-size: 46px; line-height: 46px; margin-top: 1px; }

  .headline { position: absolute; left: 0; width: 684px; text-align: center; font-family: "Arimo", sans-serif; font-weight: 700; }
  .headline--sub { top: 126px; font-size: 53px; color: var(--blue-mid); letter-spacing: -0.5px; }
  .headline--main { top: 174px; font-size: 116px; color: var(--purple); letter-spacing: -3px; line-height: 1.1; }

  .tagline {
    position: absolute; left: 70px; top: 292px;
    font-family: "Roboto Condensed", sans-serif; font-size: 22px; color: var(--white);
  }
  .features {
    position: absolute; left: 0; top: 325px; width: 100%; height: 97px; background: var(--white);
    padding: 9px 0 0 103px;
    font-family: "Roboto Condensed", sans-serif; font-size: 16px; color: var(--ink); line-height: 21px;
    list-style: none;
  }
  .features li { position: relative; width: 430px; }
  .features li::before { content: ""; position: absolute; left: -20px; top: 8px; width: 6px; height: 6px; border-radius: 50%; background: var(--ink); }

  .contact-bar {
    position: absolute; left: 0; top: 422px; width: 100%; height: 72px; background: var(--blue-mid);
    color: var(--white);
  }
  .contact-bar__left { position: absolute; left: 58px; top: 12px; }
  .contact-bar__title { font-family: "Barlow Condensed", sans-serif; font-weight: 600; font-size: 18px; line-height: 22px; }
  .contact-bar__line { font-family: "Open Sans", sans-serif; font-size: 13px; line-height: 22px; }
  .contact-bar__line strong { font-weight: 600; font-size: 16px; }
  .contact-bar__divider { position: absolute; left: 397px; top: 8px; width: 2px; height: 56px; background: var(--white); }
  .contact-bar__right { position: absolute; left: 412px; top: 15px; font-family: "Open Sans", sans-serif; font-size: 15px; line-height: 20px; }

  .return-panel { position: absolute; left: 0; top: 0; width: 308px; height: 494px; background: var(--teal); }
  .return-address { position: absolute; left: 41px; top: 26px; color: var(--white); font-family: "Roboto Condensed", sans-serif; font-size: 18px; line-height: 23px; }
  .return-address__name { font-family: "Barlow Condensed", sans-serif; font-weight: 600; font-size: 25px; line-height: 30px; }
  .promo-stripes { position: absolute; left: 0; top: 0; width: 308px; height: 494px; }
  .promo-stripes text { font-family: "Roboto Condensed", sans-serif; font-weight: 700; fill: var(--ink); }
</style>
</head>
<body>
<main class="stage">

  <section class="card card--front" aria-label="Postcard front">
    <svg class="front-art" viewBox="0 0 636 494" aria-hidden="true">
      <defs>
        <linearGradient id="wave-fill" x1="0" y1="0" x2="1" y2="0">
          <stop offset="0" stop-color="#0aa0e0"/>
          <stop offset="0.55" stop-color="#0a6ab8"/>
          <stop offset="1" stop-color="#123f96"/>
        </linearGradient>
        <linearGradient id="band-fill" x1="0" y1="0" x2="1" y2="0">
          <stop offset="0" stop-color="#123f96"/>
          <stop offset="0.5" stop-color="#0aa6e8"/>
          <stop offset="1" stop-color="#6ccaf2"/>
        </linearGradient>
      </defs>
      <path d="M0 0 H636 V30 C520 22 420 60 300 100 C220 126 120 130 0 66 Z" fill="#0ab4f0"/>
      <path d="M0 0 H636 V28 C520 18 420 50 300 90 C220 114 110 116 0 52 Z" fill="url(#wave-fill)"/>
      <rect x="0" y="287" width="636" height="38" fill="url(#band-fill)"/>
      <polygon points="365,287 382,306 365,325 420,325 437,306 420,287" fill="#4cbcf0" opacity="0.7"/>
      <polygon points="485,287 502,306 485,325 540,325 557,306 540,287" fill="#8ad6f6" opacity="0.6"/>
    </svg>

    <div class="brand-name">Harlow Peak Lending Inc.</div>

    <div class="rate-badge">
      <span class="rate-badge__label">Loan rates<br>from</span>
      <span class="rate-badge__value">8%</span>
    </div>

    <h1 class="headline headline--sub">Hard Money</h1>
    <div class="headline headline--main">LOANS</div>

    <p class="tagline">We are loaning our own funds</p>

    <ul class="features">
      <li>We do a cariety of real estate secured loans including loans to buy foreclosures, short sales &amp; more.</li>
      <li>Fix &amp; Ilio Loans at 10%</li>
      <li>No appraisal, processing fees of “junk” fees</li>
    </ul>

    <footer class="contact-bar">
      <div class="contact-bar__left">
        <div class="contact-bar__title">Denver Private Money Lender</div>
        <div class="contact-bar__line">Private money for less - <strong>call us at 303-555-0147</strong></div>
      </div>
      <div class="contact-bar__divider"></div>
      <div class="contact-bar__right">
        thimble417@postvane.net<br>
        www.harlowpeaklending.com
      </div>
    </footer>
  </section>

  <section class="card card--back" aria-label="Postcard back">
    <div class="return-panel"></div>
    <address class="return-address" style="font-style: normal;">
      <div class="return-address__name">Harlow Peak Lending Inc.</div>
      2417 Larimer Way<br>
      Denver, CO 80205
    </address>
    <svg class="promo-stripes" viewBox="0 0 308 494" aria-label="Low cost hard money real estate loans">
      <polygon points="0,209 308,131 308,181 0,259" fill="var(--green)"/>
      <polygon points="0,259 308,181 308,233 0,310" fill="var(--stripe-blue)"/>
      <polygon points="0,310 308,233 308,282 0,361" fill="var(--orange)"/>
      <text x="132" y="214" font-size="38" text-anchor="middle" transform="rotate(-14 132 201)">LOW COST</text>
      <text x="145" y="262" font-size="40" text-anchor="middle" transform="rotate(-14 145 249)">HARD MONEY</text>
      <text x="157" y="309" font-size="33" text-anchor="middle" transform="rotate(-14 157 297)">REAL ESTATE LOANS</text>
    </svg>
  </section>

</main>
</body>
</html>
```